Ledgerwise 540 for Tavlo

We are looking to design a page for the mobile app. The app is intended for financial professionals and is based on a successful desktop application. The existing design will serve as a very rough guideline, but we are open to hearing ideas.
Uploaded file #1 contains a screenshot of the existing design. The workflow is as follows:
The user picks a portfolio from the Dropdown below portfolio.
The user picks a Loss Threshold, which will dictate what gets onto the bubble chart below.
Once the bubble on the chart is clicked, a text box pops up with the description of the particular crisis that the bubble represents.
Once the bubble is clicked, the right hand side bar charts are populated with moves relevant to this scenario.
The left hand pane contains two text boxes. The lower one is particularly important, because the user is able to remove scenarios or add scenarios (screen #2). Removing scenarios is simple.
Adding scenarios brings up a wizard (screen #3). It also needs to be designed consistently with the front page of the app. The wizard has different clickable categories going down the column on the left and in a row on the top. The user can pick some or all of these categories.

Notes: The app should be designed for landscape mode only. The key to keep in mind is how the user will select bubbles on the chart. Right now, it is quite easy, but with the touchscreen it may be more complicated, so please keep that in mind when designing the chart (it should still be some version of the similar chart).
*As a first pass, please submit your idea of the concept (layout/colors/buttons) without the detailed design. We will choose 1-3 concepts and then the detailed work will take place with a much higher chance of a payout.
Updates

Thank you for the first two sketches. The second one by bertrand appears to be a bit more mobile app oriented, though we are still considering both and waiting for other submissions. One request, could you rework the sketches to include a bit more of dark blue as a background?  \

Bertrand, I think that the bubbles are too small and they are missing some volume effects. Could you make them a bit more prominent (and pick some form of dark blue background) and change the color to see if they will stand out better?
 

Industry/Entity Type

Financial

Requirements
Must have
• The general outline for the bubble chart must be retained. But the actual execution may differ significantly. We are open to seeing different ideas.
The winning design will also get a contract to design the rest of the application (2 more screens), which will be worth the same as the original design.

```html
<!DOCTYPE html>
<html lang="en">
<head>
<meta charset="utf-8">
<title>Ledgerwise 540 · Stress Scenarios</title>
<link rel="stylesheet" href="https://fonts.googleapis.com/css2?family=Arimo:wght@400;700&display=swap">
<style>
  :root {
    --page-bg: #4f4e63;
    --panel-bg: #f3f3f3;
    --tab-bg: #000000;
    --tab-text: #ffffff;
    --navy: #1a1650;
    --grid: #2a2870;
    --tooltip-bg: #55546a;
    --tooltip-line: #d8d8e0;
    --side-bg: #c8c8c8;
    --label-bg: #d6d6d6;
    --field-bg: #ffffff;
    --button-bg: #c9c9c9;
    --text-dark: #111111;
  }
  * { box-sizing: border-box; margin: 0; padding: 0; }
  html, body { width: 1200px; height: 900px; overflow: hidden; }
  body {
    position: relative;
    background: var(--page-bg);
    font-family: "Arimo", Arial, sans-serif;
    color: var(--text-dark);
  }
  .abs { position: absolute; }

  .tool-button {
    position: absolute; top: 12px; width: 60px; height: 60px;
    background: #ffffff; border-radius: 12px;
    box-shadow: 0 0 0 2px #4f4e63, 0 0 0 3px #d0d0d8;
    display: flex; align-items: center; justify-content: center;
  }
  .tool-button .inner {
    width: 52px; height: 52px; border-radius: 9px;
    border: 1px solid #9a9aa6; background: #f0f0f0;
    display: flex; align-items: center; justify-content: center;
  }
  .tool-field {
    position: absolute; top: 32px; height: 23px;
    background: var(--field-bg); border: 1px solid #9a9aa6;
    font-size: 13px; font-weight: 700; padding: 4px 0 0 5px;
  }
  .dollar { font-size: 34px; font-weight: 400; line-height: 1; }

  .side-tab {
    position: absolute; background: var(--tab-bg); color: var(--tab-text);
    font-size: 13px; font-weight: 400; letter-spacing: 0.3px;
    display: flex; align-items: center; justify-content: center;
  }
  .side-tab span { writing-mode: vertical-rl; transform: rotate(180deg); white-space: nowrap; }

  .chart-panel { left: 149px; top: 78px; width: 966px; height: 732px; background: var(--panel-bg); }

  .axis-label { position: absolute; font-size: 13px; letter-spacing: 0.3px; }
  .axis-y { left: 165px; top: 420px; transform: translate(-50%, -50%) rotate(-90deg) translateX(0); white-space: nowrap; transform-origin: center; }

  .tooltip {
    position: absolute; left: 586px; top: 430px; width: 188px; height: 110px;
    background: var(--tooltip-bg); border: 1px solid var(--tooltip-line);
    color: #ffffff; font-size: 9.5px; line-height: 13px; padding: 8px 0 0 14px;
  }
  .tooltip .name { display: inline-block; border-bottom: 1px solid #ffffff; padding: 0 4px 3px 4px; margin-bottom: 12px; }

  .contribution-panel { left: 795px; top: 78px; width: 405px; height: 365px; background: var(--side-bg); }
  .contribution-list { left: 936px; top: 90px; width: 264px; height: 331px; background: #ffffff; }
  .bar-row { position: absolute; left: 0; height: 12px; display: flex; align-items: center; }
  .bar { height: 12px; background: var(--navy); }
  .bar-value { background: var(--label-bg); font-size: 9.5px; padding: 1px 4px; height: 12px; line-height: 10px; }

  .read-model {
    left: 581px; top: 820px; width: 116px; height: 58px;
    background: var(--button-bg); border-radius: 10px;
    font-size: 19px; line-height: 24px; text-align: center; padding-top: 5px;
  }
</style>
</head>
<body>
  <!-- toolbar -->
  <div class="tool-button" style="left:152px"><div class="inner">
    <svg width="36" height="32" viewBox="0 0 36 32" aria-hidden="true">
      <rect x="1" y="1" width="34" height="30" fill="#fff" stroke="#333"/>
      <rect x="1" y="1" width="34" height="5" fill="#333"/>
      <g stroke="#333" stroke-width="1">
        <line x1="6.6" y1="6" x2="6.6" y2="31"/><line x1="12.3" y1="6" x2="12.3" y2="31"/>
        <line x1="18" y1="6" x2="18" y2="31"/><line x1="23.7" y1="6" x2="23.7" y2="31"/>
        <line x1="29.4" y1="6" x2="29.4" y2="31"/>
        <line x1="1" y1="11" x2="35" y2="11"/><line x1="1" y1="16" x2="35" y2="16"/>
        <line x1="1" y1="21" x2="35" y2="21"/><line x1="1" y1="26" x2="35" y2="26"/>
      </g>
    </svg>
  </div></div>
  <div class="tool-field" style="left:214px;width:82px">6/18/2013</div>

  <div class="tool-button" style="left:307px"><div class="inner">
    <svg width="38" height="30" viewBox="0 0 38 30" aria-hidden="true">
      <path d="M1 4 H13 L16 1 H37 V29 H1 Z" fill="#fff" stroke="#555"/>
      <line x1="1" y1="6" x2="37" y2="6" stroke="#555"/>
    </svg>
  </div></div>
  <div class="tool-field" style="left:374px;width:111px">MAM AA</div>

  <div class="tool-button" style="left:509px"><div class="inner"><span class="dollar">$</span></div></div>
  <div class="tool-field" style="left:574px;width:71px">USD</div>

  <!-- left tab -->
  <div class="side-tab" style="left:0;top:78px;width:45px;height:365px"><span>SHOCKS</span></div>

  <!-- chart -->
  <div class="abs chart-panel"></div>
  <svg class="abs" style="left:0;top:0" width="1200" height="900" aria-label="Scenario bubble chart of loss against correlation surprise">
    <defs>
      <filter id="bubble-shadow" x="-50%" y="-50%" width="200%" height="200%">
        <feDropShadow dx="1" dy="2" stdDeviation="1.5" flood-color="#000" flood-opacity="0.45"/>
      </filter>
    </defs>
    <g stroke="var(--grid)" stroke-width="0.6">
      <line x1="275" y1="135" x2="275" y2="750"/><line x1="327" y1="135" x2="327" y2="750"/>
      <line x1="379" y1="135" x2="379" y2="750"/><line x1="431" y1="135" x2="431" y2="750"/>
      <line x1="483" y1="135" x2="483" y2="750"/><line x1="535" y1="135" x2="535" y2="750"/>
      <line x1="587" y1="135" x2="587" y2="750"/><line x1="639" y1="135" x2="639" y2="750"/>
      <line x1="691" y1="135" x2="691" y2="750"/><line x1="743" y1="135" x2="743" y2="750"/>
      <line x1="795" y1="135" x2="795" y2="750"/><line x1="847" y1="135" x2="847" y2="750"/>
      <line x1="899" y1="135" x2="899" y2="750"/><line x1="951" y1="135" x2="951" y2="750"/>
      <line x1="1003" y1="135" x2="1003" y2="750"/><line x1="1050" y1="135" x2="1050" y2="750"/>
      <line x1="230" y1="135" x2="1050" y2="135"/><line x1="230" y1="170" x2="1050" y2="170"/>
      <line x1="230" y1="209" x2="1050" y2="209"/><line x1="230" y1="248" x2="1050" y2="248"/>
      <line x1="230" y1="287" x2="1050" y2="287"/><line x1="230" y1="326" x2="1050" y2="326"/>
      <line x1="230" y1="366" x2="1050" y2="366"/><line x1="230" y1="405" x2="1050" y2="405"/>
      <line x1="230" y1="444" x2="1050" y2="444"/><line x1="230" y1="483" x2="1050" y2="483"/>
      <line x1="230" y1="523" x2="1050" y2="523"/><line x1="230" y1="562" x2="1050" y2="562"/>
      <line x1="230" y1="601" x2="1050" y2="601"/><line x1="230" y1="640" x2="1050" y2="640"/>
      <line x1="230" y1="679" x2="1050" y2="679"/><line x1="230" y1="719" x2="1050" y2="719"/>
    </g>
    <g stroke="var(--navy)" stroke-width="2">
      <line x1="231" y1="135" x2="231" y2="751"/><line x1="230" y1="750" x2="1050" y2="750"/>
    </g>
    <!-- tooltip pointer -->
    <path d="M560 538 L590 506 L620 506 Z" fill="var(--tooltip-bg)" stroke="var(--tooltip-line)"/>
    <g filter="url(#bubble-shadow)">
      <circle cx="553" cy="546" r="16" fill="var(--navy)" stroke="#fff" stroke-width="2"/>
      <circle cx="553" cy="546" r="17.5" fill="none" stroke="#222" stroke-width="1"/>
      <circle cx="354" cy="679" r="16" fill="#222" stroke="#fff" stroke-width="2"/>
      <circle cx="354" cy="679" r="17.5" fill="none" stroke="#222" stroke-width="1"/>
    </g>
  </svg>
  <div class="axis-label axis-y">CORRELATION SURPRISE</div>
  <div class="axis-label" style="left:619px;top:771px">LOSS</div>

  <div class="tooltip">
    <div class="name">NAME: STAGFLATION SEVERE</div>
    <div>LOSS: -18.82</div>
    <div>PLAUSIBILITY: 0.00</div>
    <div>CORRELATION SURPRISE: -18.82</div>
  </div>

  <!-- highest contributions -->
  <div class="abs contribution-panel"></div>
  <div class="side-tab" style="left:756px;top:78px;width:40px;height:365px"><span>ASSET CONTRIBUTION 10 HIGHEST</span></div>
  <div class="abs contribution-list">
    <div class="bar-row" style="top:12px"><div class="bar" style="width:213px"></div><div class="bar-value">0.083</div></div>
    <div class="bar-row" style="top:45px"><div class="bar" style="width:179px"></div><div class="bar-value">0.071</div></div>
    <div class="bar-row" style="top:77px"><div class="bar" style="width:140px"></div><div class="bar-value">0.038</div></div>
    <div class="bar-row" style="top:109px"><div class="bar" style="width:91px"></div><div class="bar-value">0.017</div></div>
    <div class="bar-row" style="top:142px"><div class="bar" style="width:80px"></div><div class="bar-value">0.016</div></div>
    <div class="bar-row" style="top:174px"><div class="bar" style="width:67px"></div><div class="bar-value">0.009</div></div>
    <div class="bar-row" style="top:206px"><div class="bar" style="width:67px"></div><div class="bar-value">0.009</div></div>
    <div class="bar-row" style="top:238px"><div class="bar" style="width:25px"></div><div class="bar-value">0.002</div></div>
    <div class="bar-row" style="top:271px"><div class="bar" style="width:25px"></div><div class="bar-value">0.002</div></div>
    <div class="bar-row" style="top:303px"><div class="bar" style="width:16px"></div><div class="bar-value">0.001</div></div>
  </div>

  <!-- lowest contributions tab -->
  <div class="side-tab" style="left:1158px;top:443px;width:42px;height:367px"><span>ASSET CONTRIBUTION 10 LOWEST</span></div>

  <div class="abs read-model">READ<br>MODEL</div>
</body>
</html>
```